table invoices in a modern format! (make it fun to look at!!)

Our has invoices that are shown to our clients. This is currently done in a normal table view, but its boring to look at and is not modern.
We would like to have a modern look and feel
it should ABSOLUTLY not be in table form.
Cards, graphs, pictures, whatever... should be fun and almost interactive.

the table file is how it current looks like.
the other two files were "ideas" to have a better representation
IT DOES NOT NEED TO LOOK LIKE THAT if you have a better idea please go for it.

secondary objective, the graphs/cards/whatever you design should be interactive, meaning I can "click on it" to pay a bill, or see more info.

Let me know if there are more questions!

```html
<!DOCTYPE html>
<html lang="en">
<head>
<meta charset="utf-8">
<title>Invoices Prior to 2019</title>
<link href="https://fonts.googleapis.com/css2?family=Roboto:wght@400;500;700&display=swap" rel="stylesheet">
<style>
  :root{
    --ink:#111;
    --muted:#8a8a8a;
    --label:#444;
    --blue:#1aa7f7;
    --tab-active:#fdf76a;
    --orange:#f5b800;
    --green:#5ad020;
    --red:#ec5a4b;
    --red-text:#e8141b;
    --purple-a:#a066f2;
    --purple-b:#6a2de2;
    --coral-a:#f28373;
    --coral-b:#e0392f;
    --gold-a:#f9cc00;
    --gold-b:#f4a200;
    --card:#fff;
  }
  *{box-sizing:border-box;margin:0;padding:0}
  html,body{width:851px;height:1200px;overflow:hidden;background:#fff}
  body{font-family:"Roboto",Arial,sans-serif;color:var(--ink);position:relative}

  .page-title{position:absolute;left:86px;top:28px;font-size:22.5px;font-weight:400}
  .year-overview{position:absolute;left:642px;top:26px;width:143px;height:38px;border:2px solid var(--orange);border-radius:19px;
    color:var(--orange);font-size:14px;display:flex;align-items:center;justify-content:center;background:#fff;cursor:pointer}

  .year-tabs{position:absolute;left:80px;top:80px;width:703px;height:51px;background:var(--blue);display:flex;align-items:center}
  .year-tab{font-size:16px;color:#fff;position:absolute;top:15px}
  .year-tab.active{left:0;top:0;width:92px;height:51px;background:var(--tab-active);color:var(--ink);display:flex;align-items:center;justify-content:center}
  .year-tab.active::after{content:"";position:absolute;left:42px;bottom:-11px;border-left:9px solid transparent;border-right:9px solid transparent;border-top:11px solid var(--tab-active)}

  .summary{position:absolute;top:153px;height:174px;border-radius:25px;color:#fff;text-align:center;cursor:pointer}
  .summary svg{position:absolute;left:50%;transform:translateX(-50%);top:24px}
  .summary .label{position:absolute;left:0;right:0;top:90px;font-size:17px;font-weight:700;opacity:.6}
  .summary .value{position:absolute;left:0;right:0;top:114px;font-size:24px;font-weight:700}
  .summary.payment{left:80px;width:161px;background:linear-gradient(180deg,var(--purple-a),var(--purple-b))}
  .summary.total{left:260px;width:161px;background:linear-gradient(180deg,var(--coral-a),var(--coral-b))}
  .summary.balance{left:440px;width:161px;background:linear-gradient(180deg,var(--gold-a),var(--gold-b))}
  .summary.wallet{left:620px;width:158px;border:3px solid var(--green);background:#fff;color:var(--green)}
  .summary.wallet svg{top:18px}
  .summary.wallet .value{top:100px;font-size:18px;opacity:1}

  .invoices{position:absolute;left:76px;top:363px;display:grid;grid-template-columns:repeat(3,224px);grid-auto-rows:239px;column-gap:20px;row-gap:20px}
  .invoice{position:relative;background:var(--card);border-radius:25px;box-shadow:0 0 6px rgba(0,0,0,.12);overflow:hidden;cursor:pointer}
  .invoice .number{position:absolute;left:30px;top:17px;font-size:13px;color:var(--muted)}
  .invoice .period{position:absolute;left:30px;top:37px;font-size:17px}
  .invoice .rule{position:absolute;left:25px;top:64px;width:175px;height:1px;background:#ccc}
  .invoice dl{position:absolute;left:30px;top:78px;right:0}
  .invoice .row{display:flex;height:27px;align-items:center}
  .invoice dt{width:120px;font-size:11px;color:var(--label)}
  .invoice dd{font-size:11px;font-weight:700;color:#333}
  .invoice .row.open dt{font-size:13px}
  .invoice .row.open dd{font-size:14px}
  .pos{color:var(--green)!important}
  .neg{color:var(--red-text)!important}
  .zero{color:var(--muted)!important;font-weight:500!important}
  .invoice .status{position:absolute;left:0;right:0;bottom:0;height:41px;display:flex;align-items:center;justify-content:space-between;padding:0 16px 0 23px;color:#fff}
  .status strong{font-size:20px;font-weight:700}
  .status span{font-size:12.5px;font-weight:700}
  .status.paid{background:var(--green)}
  .status.partial{background:var(--orange)}
  .status.unpaid{background:var(--red)}
</style>
</head>
<body>
  <h1 class="page-title">Invoices Prior to 2019</h1>
  <a class="year-overview">Year Overview</a>

  <nav class="year-tabs">
    <span class="year-tab active">2019</span>
    <span class="year-tab" style="left:109px">2020</span>
    <span class="year-tab" style="left:181px">2021</span>
    <span class="year-tab" style="left:254px">2022</span>
    <span class="year-tab" style="left:326px">2023</span>
  </nav>

  <section class="summary payment">
    <svg width="58" height="54" viewBox="0 0 58 54" fill="none" stroke="#fff" stroke-width="3" stroke-linejoin="round">
      <path d="M3 22 L29 4 L55 22 V50 H3 Z"/><path d="M3 22 L29 38 L55 22"/><path d="M3 50 L22 34 M55 50 L36 34"/>
      <rect x="13" y="8" width="32" height="20" fill="#8a4ee9"/>
      <text x="29" y="25" text-anchor="middle" font-size="18" fill="#fff" stroke="none" font-family="Roboto,sans-serif">$</text>
    </svg>
    <div class="label">Payment</div>
    <div class="value">€ 10651.94</div>
  </section>

  <section class="summary total">
    <svg width="50" height="56" viewBox="0 0 50 56" fill="none" stroke="#fff" stroke-width="3" stroke-linejoin="round">
      <path d="M17 4 L25 9 L33 4 L30 16 H20 Z"/>
      <path d="M20 16 C6 24 2 38 4 46 C5 52 10 54 25 54 C40 54 45 52 46 46 C48 38 44 24 30 16"/>
      <text x="25" y="45" text-anchor="middle" font-size="22" font-weight="700" fill="#fff" stroke="none" font-family="Roboto,sans-serif">$</text>
    </svg>
    <div class="label">Total Price</div>
    <div class="value">€ 7849.08</div>
  </section>

  <section class="summary balance">
    <svg width="58" height="58" viewBox="0 0 58 58" fill="none" stroke="#fff" stroke-width="3" stroke-linejoin="round">
      <rect x="28" y="3" width="26" height="52"/><rect x="20" y="8" width="22" height="34" transform="rotate(-12 31 25)"/>
      <circle cx="41" cy="26" r="5"/>
      <rect x="3" y="36" width="9" height="18"/><path d="M12 38 H26 C30 38 34 40 36 44 H46 M12 52 H44"/>
      <path d="M7 41 V46 M7 49 V50"/>
    </svg>
    <div class="label">Balance</div>
    <div class="value">2802.86</div>
  </section>

  <section class="summary wallet">
    <svg width="54" height="60" viewBox="0 0 54 60" fill="none" stroke="var(--green)" stroke-width="3" stroke-linejoin="round">
      <path d="M3 24 H48 V56 H3 Z"/><path d="M40 34 H51 V46 H40 Z"/>
      <path d="M16 24 L32 3 L44 10 L34 24"/><path d="M24 24 L36 8 M30 24 L40 12"/>
      <path d="M3 24 L10 16 H18"/>
    </svg>
    <div class="value">Move to Wallet</div>
  </section>

  <main class="invoices">
    <article class="invoice">
      <div class="number">TKZ19-0037</div><h2 class="period" style="font-weight:400">Jan 2019 ZML</h2><div class="rule"></div>
      <dl>
        <div class="row"><dt>Contract Price</dt><dd>€1152.00</dd></div>
        <div class="row"><dt>Extra After Credit</dt><dd>€1411.8</dd></div>
        <div class="row"><dt>Payment Received</dt><dd>€1243.20</dd></div>
        <div class="row open"><dt>Open Balance</dt><dd class="neg">€-49.98</dd></div>
      </dl>
      <div class="status partial"><strong>Partial</strong><span>225 day later</span></div>
    </article>
    <article class="invoice">
      <div class="number">TKZ19-0037</div><h2 class="period" style="font-weight:400">Feb 2019 ZML</h2><div class="rule"></div>
      <dl>
        <div class="row"><dt>Contract Price</dt><dd>€1152.00</dd></div>
        <div class="row"><dt>Extra After Credit</dt><dd>€1411.8</dd></div>
        <div class="row"><dt>Payment Received</dt><dd>€1243.20</dd></div>
        <div class="row open"><dt>Open Balance</dt><dd class="pos">€49.98</dd></div>
      </dl>
      <div class="status paid"><strong>Paid</strong></div>
    </article>
    <article class="invoice">
      <div class="number">TKZ19-0037</div><h2 class="period" style="font-weight:400">Mar 2019 ZML</h2><div class="rule"></div>
      <dl>
        <div class="row"><dt>Contract Price</dt><dd>€1152.00</dd></div>
        <div class="row"><dt>Extra After Credit</dt><dd>€1411.8</dd></div>
        <div class="row"><dt>Payment Received</dt><dd>€1243.20</dd></div>
        <div class="row open"><dt>Open Balance</dt><dd class="zero">€0.00</dd></div>
      </dl>
      <div class="status paid"><strong>Paid</strong></div>
    </article>

    <article class="invoice">
      <div class="number">TKZ19-0037</div><h2 class="period" style="font-weight:400">Apr 2019 ZML</h2><div class="rule"></div>
      <dl>
        <div class="row"><dt>Contract Price</dt><dd class="pos">€1152.00 Pay</dd></div>
        <div class="row"><dt>Extra After Credit</dt><dd>€1411.8</dd></div>
        <div class="row"><dt>Payment Received</dt><dd>€1243.20</dd></div>
        <div class="row open"><dt>Open Balance</dt><dd class="neg">€-49.98</dd></div>
      </dl>
      <div class="status unpaid"><strong>Unpaid</strong><span>135 day later</span></div>
    </article>
    <article class="invoice">
      <div class="number">TKZ19-0037</div><h2 class="period" style="font-weight:400">May 2019 LRZ</h2><div class="rule"></div>
      <dl>
        <div class="row"><dt>Contract Price</dt><dd>€1152.00</dd></div>
        <div class="row"><dt>Extra After Credit</dt><dd>€1411.8</dd></div>
        <div class="row"><dt>Payment Received</dt><dd>€1243.20</dd></div>
        <div class="row open"><dt>Open Balance</dt><dd class="neg">€-49.98</dd></div>
      </dl>
      <div class="status partial"><strong>Partial</strong><span>104 day later</span></div>
    </article>
    <article class="invoice">
      <div class="number">TKZ19-0037</div><h2 class="period" style="font-weight:400">Jun 2019 LRZ</h2><div class="rule"></div>
      <dl>
        <div class="row"><dt>Contract Price</dt><dd>€1152.00</dd></div>
        <div class="row"><dt>Extra After Credit</dt><dd>€1411.8</dd></div>
        <div class="row"><dt>Payment Received</dt><dd>€1243.20</dd></div>
        <div class="row open"><dt>Open Balance</dt><dd class="pos">€49.98</dd></div>
      </dl>
      <div class="status paid"><strong>Paid</strong></div>
    </article>

    <article class="invoice">
      <div class="number">TKZ19-0037</div><h2 class="period" style="font-weight:400">Jul 2019 LRZ</h2><div class="rule"></div>
      <dl>
        <div class="row"><dt>Contract Price</dt><dd>€1152.00</dd></div>
        <div class="row"><dt>Extra After Credit</dt><dd>€1411.8</dd></div>
        <div class="row"><dt>Payment Received</dt><dd>€1243.20</dd></div>
        <div class="row open"><dt>Open Balance</dt><dd class="pos">€49.98</dd></div>
      </dl>
      <div class="status paid"><strong>Paid</strong></div>
    </article>
    <article class="invoice">
      <div class="number">TKZ19-0037</div><h2 class="period" style="font-weight:400">Aug 2019 LRZ</h2><div class="rule"></div>
      <dl>
        <div class="row"><dt>Contract Price</dt><dd class="pos">€1152.00 Pay</dd></div>
        <div class="row"><dt>Extra After Credit</dt><dd>€1411.8</dd></div>
        <div class="row"><dt>Payment Received</dt><dd>€1243.20</dd></div>
        <div class="row open"><dt>Open Balance</dt><dd class="neg">€-1222.65</dd></div>
      </dl>
      <div class="status unpaid"><strong>Unpaid</strong><span>13 day later</span></div>
    </article>
    <article class="invoice">
      <div class="number">TKZ19-0037</div><h2 class="period" style="font-weight:400">Sep 2019 LRZ</h2><div class="rule"></div>
      <dl>
        <div class="row"><dt>Contract Price</dt><dd>€1152.00</dd></div>
        <div class="row"><dt>Extra After Credit</dt><dd>€1411.8</dd></div>
        <div class="row"><dt>Payment Received</dt><dd>€1243.20</dd></div>
        <div class="row open"><dt>Open Balance</dt><dd class="zero">€-59113</dd></div>
      </dl>
      <div class="status paid"><strong>Paid</strong></div>
    </article>
  </main>
</body>
</html>
```